Rig up a website for a Rigging Company

We already have a logo. Looking for a website design that works on plinvara.com.
Our rigging company uses semi trucks, forklifts, and similar equipment to move large machines.
Our logo is white, black and red.

Target Market(s)

Medical Industry (moving medical equipment), Utility Industry (power equipment), Food Industry (moving bottling/packing equipment), US Government (large equipment)

Industry/Entity Type

It Company

Coding

Coded - Design and coding required

Number of Pages Required

5+ page

Font styles to use
Sans Serif

Colors
ec1f27
ffffff
0355a3

Requirements
Must have
• Home page, About page, Services Page, and Contact Information page
Nice to have
• Pictures of semi and forklifts and ability to insert our own pictures of our equipment

```html
<!DOCTYPE html>
<html lang="en">
<head>
<meta charset="utf-8">
<title>Holt Rigging</title>
<link rel="stylesheet" href="https://fonts.googleapis.com/css2?family=Raleway:ital,wght@0,400;0,500;0,700;1,700&family=Open+Sans:wght@400;600;700&display=swap">
<style>
:root{
  --red:#d3212b;
  --red-dark:#a8161e;
  --black:#0b0b0b;
  --ink:#222;
  --grey:#666;
  --light:#e9e9e9;
  --white:#fff;
  --steel:#3a3a3a;
}
*{box-sizing:border-box;margin:0;padding:0}
html,body{width:1200px;height:3974px;overflow:hidden}
body{position:relative;background:var(--white);font-family:"Open Sans",Arial,sans-serif;color:var(--ink)}
.abs{position:absolute}
.topbar{left:0;top:0;width:1200px;height:34px;background:var(--black);color:#ddd;font-size:12px}
.topbar .mail{left:111px;top:9px}
.topbar .phone{left:610px;top:9px}
.topbar .social{right:111px;top:8px;display:flex;gap:8px}
.dot-icon{width:18px;height:18px;border-radius:50%;background:#ddd}
.hero{left:0;top:34px;width:1200px;height:608px;background:linear-gradient(100deg,#3d3d3d 0%,#4c4c4c 45%,#2e2e2e 100%)}
.hero-photo{left:430px;top:120px;width:680px;height:480px;background:radial-gradient(ellipse at 60% 55%,#8a7a4a 0%,#4a463c 45%,rgba(60,60,60,0) 75%)}
.logo{left:111px;top:40px;width:239px;height:119px;background:var(--white);display:flex;align-items:center;justify-content:center;gap:10px}
.logo span{font-family:"Raleway",sans-serif;font-weight:700;font-size:30px;color:var(--red)}
.logo i{width:16px;height:16px;background:var(--black);display:block}
.nav{left:566px;top:78px;display:flex;gap:46px;font-family:"Raleway",sans-serif;font-weight:700;font-size:15px;color:var(--white);letter-spacing:1px}
.nav .active{border-bottom:2px solid var(--white);padding-bottom:8px}
.hero-title{left:116px;top:292px;font-family:"Raleway",sans-serif;font-style:italic;font-weight:700;font-size:40px;color:var(--white)}
.hero-sub{left:116px;top:346px;font-family:"Raleway",sans-serif;font-style:italic;font-weight:700;font-size:17px;line-height:22px;color:var(--white)}
.btn{display:flex;align-items:center;justify-content:center;border:2px solid var(--white);color:var(--white);font-family:"Raleway",sans-serif;font-weight:700;font-size:13px;letter-spacing:1px}
.hero .btn{left:284px;top:371px;width:132px;height:36px}
.about{left:125px;top:615px;width:951px;height:241px;background:var(--red);color:var(--white);text-align:center}
.about-head{left:0;top:0;width:951px;height:12px;border-top:10px solid #e9e9e9}
.about h2{position:absolute;left:0;right:0;top:28px;font-family:"Raleway",sans-serif;font-weight:500;font-size:20px;letter-spacing:3px}
.about .rule{position:absolute;left:365px;top:64px;width:220px;height:12px}
.about p{position:absolute;left:70px;right:70px;top:88px;font-size:13px;line-height:19px;font-weight:600}
.about .btn{position:absolute;left:411px;top:180px;width:130px;height:38px}
.section-title{left:0;width:1200px;text-align:center;font-family:"Raleway",sans-serif;font-weight:500;font-size:27px;letter-spacing:2px;color:var(--ink)}
.rule-dark{left:480px;width:240px;height:14px}
.services{left:110px;top:1050px;width:980px;display:flex;justify-content:space-between}
.service{width:230px;text-align:center}
.service svg{height:60px}
.service h3{margin-top:20px;font-family:"Raleway",sans-serif;font-weight:700;font-size:17px;letter-spacing:1.5px;font-style:italic;color:var(--ink)}
.service p{margin-top:14px;font-size:12px;line-height:17px;color:var(--grey)}
.tagline{left:0;width:1200px;top:1296px;text-align:center;font-size:10px;font-style:italic;font-weight:700;color:var(--ink)}
.tagline b{color:var(--red)}
.pager{display:flex;gap:10px}
.pager i{width:16px;height:16px;border-radius:50%;background:#ccc;display:block}
.pager i.on{background:var(--red-dark)}
.filters{left:0;width:1200px;top:1488px;display:flex;justify-content:center;gap:32px;font-family:"Raleway",sans-serif;font-weight:700;font-size:13px;letter-spacing:1px}
.filters .on{color:var(--red)}
.gallery{left:111px;top:1556px;width:978px;display:grid;grid-template-columns:repeat(4,1fr);gap:9px}
.gallery div{height:197px}
.results{left:0;top:2260px;width:1200px;height:422px;background:linear-gradient(90deg,#2a2a2a 0%,#3c3c3c 60%,#222 100%)}
.results h2{position:absolute;left:111px;top:120px;font-family:"Raleway",sans-serif;font-weight:500;font-size:26px;letter-spacing:1.5px;color:var(--white)}
.results p{position:absolute;left:111px;top:160px;width:470px;font-size:13px;line-height:19px;color:var(--white)}
.results .btn{position:absolute;left:111px;top:268px;width:140px;height:38px}
.stat{width:221px;height:146px;display:flex;flex-direction:column;align-items:center;justify-content:center;color:var(--white)}
.stat b{font-size:26px;font-family:"Raleway",sans-serif}
.stat span{font-size:13px;margin-top:8px}
.stat.red{background:rgba(200,30,40,.88)}
.stat.dark{background:rgba(20,20,20,.7)}
.kicker{left:0;width:1200px;top:2760px;text-align:center;font-size:14px;color:var(--ink)}
.card{top:2883px;height:310px;background:var(--white);box-shadow:0 0 6px rgba(0,0,0,.08);text-align:center}
.avatar{position:absolute;left:50%;top:24px;margin-left:-42px;width:84px;height:84px;border-radius:50%;border:3px solid #ddd;background:linear-gradient(#c9b9a4,#7c6c5c)}
.card h4{position:absolute;left:0;right:0;top:128px;font-size:13px;font-weight:600}
.card .role{position:absolute;left:0;right:0;top:150px;font-size:11px;color:var(--grey)}
.card p{position:absolute;left:40px;right:40px;top:200px;font-size:12px;line-height:17px;color:var(--grey)}
.newsletter{left:0;top:3304px;width:1200px;height:213px;background:linear-gradient(90deg,#c61d27,#d8323a 60%,#b5181f)}
.newsletter h2{position:absolute;left:0;right:0;top:32px;text-align:center;font-family:"Raleway",sans-serif;font-weight:500;font-size:27px;letter-spacing:2px;color:var(--white)}
.newsletter h3{position:absolute;left:0;right:0;top:70px;text-align:center;font-family:"Raleway",sans-serif;font-weight:500;font-size:16px;letter-spacing:2px;color:var(--white)}
.form{position:absolute;left:366px;top:109px;width:509px;height:40px;background:var(--white);display:flex;align-items:center;padding:6px}
.form .field{flex:1;font-size:10px;color:#999;padding-left:10px}
.form .submit{width:110px;height:26px;background:var(--red);color:var(--white);font-weight:700;font-size:12px;display:flex;align-items:center;justify-content:center;letter-spacing:1px}
.contact-col{top:3665px;width:320px;text-align:center}
.circle{width:82px;height:82px;border-radius:50%;background:var(--black);margin:0 auto;display:flex;align-items:center;justify-content:center}
.contact-col h5{margin-top:26px;font-size:14px;font-weight:700;letter-spacing:1px}
.contact-col p{margin-top:10px;font-size:15px;line-height:22px;color:#444}
.mini{display:flex;justify-content:center;gap:8px;margin-top:10px}
.mini i{width:22px;height:22px;border-radius:50%;background:var(--black);display:block}
.footer{left:0;top:3922px;width:1200px;height:52px;background:var(--black);color:var(--white);font-size:12px;font-weight:700}
.footer span{position:absolute;left:111px;top:18px}
</style>
</head>
<body>

<div class="abs topbar">
  <span class="abs mail">info@plinvara.com</span>
  <span class="abs phone">123-456-7890</span>
  <div class="abs social"><i class="dot-icon"></i><i class="dot-icon"></i><i class="dot-icon"></i><i class="dot-icon"></i><i class="dot-icon"></i></div>
</div>

<header class="abs hero">
  <div class="abs hero-photo" role="img" aria-label="Yellow and grey forklift in a dark concrete warehouse"></div>
  <div class="abs logo" style="top:6px"><i></i><span>Holt Rigging</span></div>
  <nav class="abs nav" style="top:44px"><span class="active">HOME</span><span>ABOUT</span><span>SERVICES</span><span>CONTACT</span><span>BLOG</span></nav>
  <h1 class="abs hero-title" style="top:258px">Welcome To Holt Rigging</h1>
  <p class="abs hero-sub" style="top:310px">Lorem Ipsum is simply dummy text of the printing<br>and type setting industry.</p>
  <div class="abs btn">READ MORE</div>
</header>

<section class="abs about">
  <h2>ABOUT</h2>
  <svg class="rule" viewBox="0 0 220 12"><line x1="0" y1="6" x2="98" y2="6" stroke="#fff" stroke-width="2"/><rect x="105" y="1" width="10" height="10" fill="#fff" transform="rotate(45 110 6)"/><line x1="122" y1="6" x2="220" y2="6" stroke="#fff" stroke-width="2"/></svg>
  <p>Lorem Ipsum is simply dummy text of the printing and typesetting industry. Lorem Ipsum has been the industry's standard dummy text ever since the 1500s, when annown printer took a galley of type and scrambled it to make a type specimen book. It has survived not only five centuries, but alsothe leap into electronic typesetting, remaining essentially unchanged. It was popularised in the 1960s with the release of Letraset sheets containing Lorem Ipsum passages.</p>
  <div class="btn">READ MORE</div>
</section>

<h2 class="abs section-title" style="top:914px">WE MAKE THE BEST SERVICES</h2>
<svg class="abs rule-dark" style="top:962px" viewBox="0 0 240 14"><line x1="0" y1="7" x2="108" y2="7" stroke="#222" stroke-width="2"/><rect x="114" y="2" width="11" height="11" fill="#222" transform="rotate(45 120 7)"/><line x1="132" y1="7" x2="240" y2="7" stroke="#222" stroke-width="2"/></svg>

<div class="abs services">
  <div class="service">
    <svg viewBox="0 0 90 50"><rect x="2" y="10" width="56" height="26" fill="#d3212b"/><path d="M60 18h16l10 10v8H60z" fill="#d3212b"/><circle cx="16" cy="40" r="6" fill="#d3212b" stroke="#fff" stroke-width="2"/><circle cx="72" cy="40" r="6" fill="#d3212b" stroke="#fff" stroke-width="2"/></svg>
    <h3>SEMI TRUCKS</h3>
    <p>Lorem ipsum dolor sit amet, consectetur adipiscing elit. Morbi vel bibendum dui imperdiet fermentum molestie.</p>
  </div>
  <div class="service">
    <svg viewBox="0 0 60 60"><path d="M8 6v46h22" fill="none" stroke="#d3212b" stroke-width="4"/><path d="M18 20h16l8 16v12H18z" fill="none" stroke="#d3212b" stroke-width="4"/><circle cx="24" cy="52" r="5" fill="#d3212b"/><circle cx="42" cy="52" r="5" fill="#d3212b"/></svg>
    <h3>FORKLIFTS</h3>
    <p>Lorem ipsum dolor sit amet, consectetur adipiscing elit. Morbi vel bibendum dui imperdiet fermentum molestie.</p>
  </div>
  <div class="service">
    <svg viewBox="0 0 60 60"><path d="M14 4l8 44h26" fill="none" stroke="#d3212b" stroke-width="4"/><rect x="24" y="16" width="18" height="18" fill="none" stroke="#d3212b" stroke-width="4" transform="rotate(-12 33 25)"/><circle cx="24" cy="52" r="6" fill="none" stroke="#d3212b" stroke-width="4"/></svg>
    <h3>SIMILAR EQUIPMENT</h3>
    <p>Lorem ipsum dolor sit amet, consectetur adipiscing elit. Morbi vel bibendum dui imperdiet fermentum molestie.</p>
  </div>
  <div class="service">
    <svg viewBox="0 0 80 60"><rect x="6" y="44" width="48" height="12" rx="6" fill="#d3212b"/><rect x="16" y="26" width="26" height="16" fill="#d3212b"/><path d="M40 28l16-18 14 10" fill="none" stroke="#d3212b" stroke-width="4"/><path d="M66 20l8 14h-12z" fill="#d3212b"/></svg>
    <h3>LARGE MACHINES</h3>
    <p>Lorem ipsum dolor sit amet, consectetur adipiscing elit. Morbi vel bibendum dui imperdiet fermentum molestie.</p>
  </div>
</div>

<p class="abs tagline">We Have a Wide Range of Services <b>View Gallery</b></p>
<div class="abs pager" style="left:566px;top:1333px"><i></i><i></i><i class="on"></i></div>

<h2 class="abs section-title" style="top:1394px">GALLERY</h2>
<svg class="abs rule-dark" style="top:1442px" viewBox="0 0 240 14"><line x1="0" y1="7" x2="108" y2="7" stroke="#222" stroke-width="2"/><rect x="114" y="2" width="11" height="11" fill="#222" transform="rotate(45 120 7)"/><line x1="132" y1="7" x2="240" y2="7" stroke="#222" stroke-width="2"/></svg>

<div class="abs filters"><span class="on">ALL</span><span>VIDEO</span><span>TRUCK</span><span>FORKLIFT</span><span>SIMILAR EQUIPMENT</span><span>LARGE MACHINES</span></div>

<div class="abs gallery">
  <div role="img" aria-label="White semi truck on a highway" style="background:linear-gradient(160deg,#b9c3cc,#e6e8ea 50%,#7f8790)"></div>
  <div role="img" aria-label="Red rough terrain forklift outdoors" style="background:linear-gradient(160deg,#cfd9e2,#b23a32 55%,#5f5f55)"></div>
  <div role="img" aria-label="Yellow forklifts in a warehouse" style="background:linear-gradient(160deg,#9a9c9a,#c8a22a 55%,#555)"></div>
  <div role="img" aria-label="Warehouse worker in a hard hat and safety vest" style="background:linear-gradient(160deg,#8e9399,#d7b43a 60%,#3b4450)"></div>
  <div role="img" aria-label="Forklift in an empty industrial hall" style="background:linear-gradient(160deg,#d6d6d6,#9a9a9a 60%,#616161)"></div>
  <div role="img" aria-label="Yellow wheel loader with raised bucket" style="background:linear-gradient(160deg,#6b9bd2,#d8aa2a 60%,#6d6a55)"></div>
  <div role="img" aria-label="Yellow skid steer loader on a site" style="background:linear-gradient(160deg,#4c5668,#e2b21e 55%,#2a2a2a)"></div>
  <div role="img" aria-label="Small red forklift in a bright hall" style="background:linear-gradient(160deg,#c8c8c8,#a2342e 60%,#6d6d6d)"></div>
  <div role="img" aria-label="Yellow telescopic handler under a clear sky" style="background:linear-gradient(160deg,#8fb7e0,#d8b12b 60%,#6f6b58)"></div>
  <div role="img" aria-label="Heavy yellow container handler in the snow" style="background:linear-gradient(160deg,#dfe4ea,#cfa629 55%,#8c8c88)"></div>
  <div style="position:relative;background:var(--white)">
    <div role="img" aria-label="Dark warehouse aisle" style="position:absolute;left:0;top:0;width:100%;height:98px;background:linear-gradient(160deg,#3b3b3b,#1d1d1d)"></div>
    <div style="position:absolute;left:0;right:0;top:126px;text-align:center;font-family:'Raleway',sans-serif;font-weight:700;font-size:22px;color:#d3212b">Holt Rigging</div>
  </div>
  <div role="img" aria-label="Forklift parked in a dark storage area" style="background:linear-gradient(160deg,#4a4a4a,#8d8050 60%,#2e2e2e)"></div>
</div>

<section class="abs results" role="img" aria-label="Dark backdrop of a warehouse with a red forklift">
  <h2>WE Have Great Result</h2>
  <p>Lorem Ipsum is simply dummy text of the printing and typesetting industry. Lorem Ipsum has been the industry's standard dummy text ever since the 1500s, when annown printer took a galley of type and scrambled it to make a type specimen.</p>
  <div class="btn">READ MORE</div>
  <div class="abs stat dark" style="left:623px;top:72px"><b>5000</b><span>Successful Cases</span></div>
  <div class="abs stat red" style="left:866px;top:72px"><b>4500</b><span>Trusted Clients</span></div>
  <div class="abs stat red" style="left:623px;top:239px"><b>8100</b><span>Case Studies</span></div>
  <div class="abs stat dark" style="left:866px;top:239px"><b>1530</b><span>Registere Case</span></div>
</section>

<p class="abs kicker">Our Testimonials</p>
<h2 class="abs section-title" style="top:2784px;font-size:32px">WHAT CLIENTS SAY ABOUT US</h2>
<svg class="abs rule-dark" style="top:2838px" viewBox="0 0 240 14"><line x1="0" y1="7" x2="108" y2="7" stroke="#222" stroke-width="2"/><rect x="114" y="2" width="11" height="11" fill="#222" transform="rotate(45 120 7)"/><line x1="132" y1="7" x2="240" y2="7" stroke="#222" stroke-width="2"/></svg>

<div class="abs card" style="left:106px;width:292px"><div class="avatar" role="img" aria-label="Portrait of a client"></div><h4>Jane Doe</h4><div class="role">Enginer of Media Production</div><p>Lorem ipsum dolor sit amet, consectetur adipiscing elit. Morbi vel bibendum nullam imperdiet fermentum molestie.</p></div>
<div class="abs card" style="left:445px;width:318px"><div class="avatar" role="img" aria-label="Portrait of a client"></div><h4>Jane Dolor</h4><div class="role">Enginer of Media Production</div><p>Lorem ipsum dolor sit amet, consectetur adipiscing elit. Morbi vel bibendum nullam imperdiet fermentum molestie.</p></div>
<div class="abs card" style="left:787px;width:302px"><div class="avatar" role="img" aria-label="Portrait of a client"></div><h4>John Doe</h4><div class="role">Enginer of Media Production</div><p>Lorem ipsum dolor sit amet, consectetur adipiscing elit. Morbi vel bibendum nullam imperdiet fermentum molestie.</p></div>
<div class="abs pager" style="left:566px;top:3228px"><i></i><i></i><i class="on"></i></div>

<section class="abs newsletter" role="img" aria-label="Red tinted warehouse with forklifts">
  <h2>SUBSCRIBE TO OUR NEWSLETTER</h2>
  <h3>TO RECEIVE THE LATEST NEWS &amp; UPDATE</h3>
  <div class="form"><span class="field">Your E-Mail</span><span class="submit">SUBMIT</span></div>
</section>

<h2 class="abs section-title" style="top:3552px;font-size:30px">CONTACT</h2>
<svg class="abs rule-dark" style="top:3601px" viewBox="0 0 240 16"><line x1="0" y1="8" x2="104" y2="8" stroke="#222" stroke-width="2"/><g fill="#222"><rect x="116" y="0" width="7" height="7" transform="rotate(45 120 4)"/><rect x="116" y="9" width="7" height="7" transform="rotate(45 120 12)"/><rect x="111" y="4" width="7" height="7" transform="rotate(45 114 8)"/><rect x="121" y="4" width="7" height="7" transform="rotate(45 126 8)"/></g><line x1="136" y1="8" x2="240" y2="8" stroke="#222" stroke-width="2"/></svg>

<div class="abs contact-col" style="left:102px">
  <div class="circle"><svg width="34" height="44" viewBox="0 0 34 44"><path d="M17 2C8 2 2 9 2 17c0 11 15 25 15 25s15-14 15-25C32 9 26 2 17 2z" fill="#fff"/><circle cx="17" cy="17" r="6" fill="#0b0b0b"/></svg></div>
  <h5>ADDRESS</h5>
  <p>12345 West 23th Street,<br>Suite 123</p>
</div>
<div class="abs contact-col" style="left:440px">
  <div class="circle"><svg width="44" height="32" viewBox="0 0 44 32"><rect x="2" y="2" width="40" height="28" fill="#fff"/><path d="M2 2l20 16L42 2" fill="none" stroke="#0b0b0b" stroke-width="3"/></svg></div>
  <h5>PHONE</h5>
  <p>email@yourdomain.com</p>
  <div class="mini"><i></i><i></i><i></i><i></i><i></i></div>
</div>
<div class="abs contact-col" style="left:778px">
  <div class="circle"><svg width="44" height="40" viewBox="0 0 44 40"><path d="M4 12c0-6 36-6 36 0v4h-9v-4H13v4H4z" fill="#fff"/><path d="M10 18h24l6 18H4z" fill="#fff"/><circle cx="22" cy="27" r="5" fill="#0b0b0b"/></svg></div>
  <h5>EMAIL</h5>
  <p>+1 (0) 101 0000 000<br>+1 (0) 102 1234 567</p>
</div>

<footer class="abs footer"><span>PRIVACY POLICY · LEGAL MENTIONS · TERMS AND CONDITIONS</span></footer>

</body>
</html>
```